Non-Profit, Organic, Natural Feel, Clean & Simple Business Cards

Looking for a business card design. Has an organic, natural, new-age, clean and simple look/feel. We are a non-profit group that works with Moringa(a health plant/superfood) by spreading and sharing seeds of Moringa. A design that stands out but clean and professional. I will upload our new logo design. The font can be changed. Also I will upload some pictures of Moringa.
Our Facebook page is www.facebook.com/TulvaSproutTrust Check us out to get a feel of us.

Target Market(s)

Everyone. Movers & Shakers of The Sustainable, Natural Medicines & Cosmetics, Organic Food Farming Industry. And To The Common Person Or A Local Family.

Industry/Entity Type

Sustainability

Contact Information for Business Card

Email: TulvaSoilTrust@Brenwick.com
FB: www.Facebook.com/TulvaSproutTrust
Website: www.TulvaSproutTrust.com

Requirements
Must have
• Image/Pic/Design of Moringa Leaves. Somewhere on the card. Clean and Clear. So you could easily identify the Moringa from the Business Card. Something Alive, Living, Green Feel to the card design.
Nice to have
• A warm, friendly, professional feel to the design. A organic sustainable concept/future with Moringa is the business card impression/image we are trying to present.

```html
<!DOCTYPE html>
<html lang="en">
<head>
<meta charset="utf-8">
<title>Tulva Sprout Trust – Business Card</title>
<link rel="stylesheet" href="https://fonts.googleapis.com/css2?family=Marcellus&family=Open+Sans:wght@400&display=swap">
<style>
  :root {
    --backdrop: #e7e4de;
    --card-light: #cfcfc8;
    --card-dark: #8d8d86;
    --leaf-green: #3f8a2c;
    --leaf-deep: #2f6f22;
    --text-light: #f4f4f0;
    --text-dark: #4a4a48;
  }
  * { box-sizing: border-box; margin: 0; padding: 0; }
  html, body { width: 1200px; height: 969px; overflow: hidden; }
  body { background: var(--backdrop); position: relative; }
  .card {
    position: absolute; left: 100px; top: 200px;
    width: 1000px; height: 568px;
    background: var(--card-light);
    overflow: hidden;
    box-shadow: 0 10px 30px rgba(0,0,0,0.18);
  }
  .card-art { position: absolute; inset: 0; }
  .holder { position: absolute; left: 50px; color: var(--text-light); font-family: "Marcellus", serif; text-transform: uppercase; letter-spacing: 2px; }
  .holder-name { top: 178px; font-size: 36px; }
  .holder-role { top: 236px; font-size: 25px; }
  .contacts { position: absolute; left: 50px; top: 300px; list-style: none; font-family: "Open Sans", sans-serif; font-size: 23px; color: var(--text-light); }
  .contacts li { display: flex; align-items: center; gap: 14px; height: 42px; }
  .contacts svg { width: 24px; height: 24px; flex: none; }
  .brand { position: absolute; left: 615px; top: 252px; display: flex; align-items: center; gap: 16px; }
  .brand-square { width: 56px; height: 56px; border: 5px solid var(--leaf-green); }
  .brand-name { font-family: "Marcellus", serif; font-size: 27px; letter-spacing: 1px; color: var(--text-dark); text-transform: uppercase; white-space: nowrap; }
</style>
</head>
<body>
  <div class="card">
    <svg class="card-art" viewBox="0 0 1000 568" width="1000" height="568">
      <defs>
        <linearGradient id="leafFill" x1="0" y1="0" x2="0" y2="1">
          <stop offset="0" stop-color="#4d9a34"/>
          <stop offset="1" stop-color="#2f6f22" stop-opacity="0.8"/>
        </linearGradient>
      </defs>
      <path class="panel-left" d="M0 0 H560 C470 150 470 420 580 568 H0 Z" fill="var(--card-dark)"/>
      <path class="stem" d="M560 0 C470 150 470 420 580 568" fill="none" stroke="var(--leaf-green)" stroke-width="12"/>
      <rect class="leaf-sprig" x="480" y="0" width="120" height="150" rx="30" fill="url(#leafFill)" role="img" aria-label="Sprig of moringa leaves growing from the stem"/>
    </svg>

    <h1 class="holder holder-name">Elias Harwood</h1>
    <p class="holder holder-role">CEO/Founder</p>

    <ul class="contacts">
      <li>
        <svg viewBox="0 0 24 24" aria-hidden="true"><rect x="2" y="5" width="20" height="14" fill="none" stroke="currentColor" stroke-width="2"/><path d="M2 5 L12 13 L22 5" fill="none" stroke="currentColor" stroke-width="2"/></svg>
        TulvaSoilTrust@Brenwick.com
      </li>
      <li>
        <svg viewBox="0 0 24 24" aria-hidden="true"><circle cx="12" cy="12" r="10" fill="none" stroke="currentColor" stroke-width="2"/><ellipse cx="12" cy="12" rx="4" ry="10" fill="none" stroke="currentColor" stroke-width="1.5"/><path d="M2 12 H22" stroke="currentColor" stroke-width="1.5"/></svg>
        www.TulvaSproutTrust.com
      </li>
      <li>
        <svg viewBox="0 0 24 24" aria-hidden="true"><rect x="3" y="3" width="18" height="18" fill="currentColor"/></svg>
        /TulvaSproutTrust
      </li>
    </ul>

    <div class="brand">
      <span class="brand-square"></span>
      <span class="brand-name">Tulva Sprout Trust</span>
    </div>
  </div>
</body>
</html>
```